Advertising brochure for Trail Along Southside

We need a new single sided DL flier for the 2020 season!<br/>This flier is for our tour business. You can find all the details about the tour at our web site http://trailalong.southside.example<br/>The flier needs to grab the tourists attention, explain the tour and give price. I will upload a copy of last year's flier for your reference.<br/>We'd like the flier to match our web site to some extent.<br/>The most up to date information is on the web site and NOT last year's brochure. Use the web site for tour itinerary. We NO LONGER do the "Orchard Walk".<br/>Remember the size is "DL". Please no A4 format etc.<br/>You will be able to source images from:<br/>- Our web site<br/>- Our Chatterbook<br/>- Roamreview<br/>- Quarrel Listings<br/>If you have a particular idea in mind then feel free to contact us and we will try to accommodate your photo request.<br/>Good luck!

Target Market(s)

All ages

Industry/Entity Type

Tourism

Requirements
Must have
• Phone number
• Web Site
• Email address
• Price
Nice to have
• Description of tour and images

```html
<!DOCTYPE html>
<html lang="en">
<head>
<meta charset="utf-8">
<title>Trail Along Southside – DL Flier</title>
<link href="https://fonts.googleapis.com/css2?family=Montserrat:wght@400;500;600;700&family=Poppins:wght@500;700;800&display=swap" rel="stylesheet">
<style>
:root{
  --orange:#f28705;
  --ink:#3a2418;
  --body:#2b2b2b;
  --sky-top:#c9a7a0;
  --sky-glow:#f3a565;
  --earth:#8a4e2e;
  --earth-dark:#5c3220;
  --paper:#ffffff;
  --stage:#2a2a2a;
}
*{margin:0;padding:0;box-sizing:border-box}
html,body{width:1200px;height:857px;overflow:hidden;background:var(--stage)}
body{font-family:"Montserrat",sans-serif;display:flex;align-items:center;justify-content:center}
.flier{position:relative;width:372px;height:826px;background:var(--paper);overflow:hidden}
.hero{position:absolute;left:0;top:0;width:100%;height:365px;
  background:linear-gradient(180deg,var(--sky-top) 0%,#e6a98a 16%,var(--sky-glow) 28%,var(--earth) 36%,#9a5a36 58%,var(--earth-dark) 78%,#fff 100%)}
.hero-fade{position:absolute;left:0;bottom:0;width:100%;height:60px;background:linear-gradient(180deg,rgba(255,255,255,0),#fff)}
.logo-badge{position:absolute;left:17px;top:17px;width:131px;height:127px;border-radius:50%;background:var(--orange);
  display:flex;align-items:center;justify-content:center;text-align:center;color:#fff;font-weight:700;font-size:14px;line-height:1.25;padding:18px}
.brand{position:absolute;left:203px;top:56px;color:var(--ink);font-weight:600;font-size:19px;line-height:1.1;width:160px}
.contact{position:absolute;left:203px;top:112px;font-size:8px;color:var(--ink);font-weight:500;line-height:1.6}
.contact li{list-style:none;display:flex;align-items:center;gap:4px}
.contact svg{width:9px;height:9px;flex:none}
.price{position:absolute;left:14px;top:160px;font-family:"Poppins",sans-serif;font-weight:800;font-size:82px;line-height:1;letter-spacing:-3px;color:#f2f2f2;
  text-shadow:3px 3px 0 var(--earth-dark)}
.per{position:absolute;left:197px;top:200px;color:#fff}
.per strong{display:block;font-family:"Poppins",sans-serif;font-weight:500;font-size:17px;line-height:1.05}
.per span{display:block;font-size:6.2px;font-weight:600;margin-top:2px;white-space:nowrap}
.intro{position:absolute;left:25px;top:367px;width:320px;border:2px solid var(--orange);border-radius:4px;padding:7px 6px 8px;text-align:center;color:var(--ink);font-size:10.4px;font-weight:500;line-height:1.4;letter-spacing:.2px}
.intro p+p{margin-top:5px}
.itinerary{position:absolute;left:31px;top:462px;width:318px;list-style:none}
.stop{display:flex;gap:10px;margin-bottom:8px}
.stop-photo{flex:0 0 73px;height:42px;border:1px solid #555}
.stop-text{width:232px}
.stop h3{font-size:9.6px;font-weight:700;color:var(--ink);margin-bottom:3px}
.stop p{font-size:6.7px;line-height:1.4;letter-spacing:.15px;color:var(--body)}
.footer{position:absolute;left:0;bottom:0;width:100%;height:20px;background:var(--orange);color:var(--ink);font-size:10px;font-weight:600;letter-spacing:.6px;display:flex;align-items:center;justify-content:center}
</style>
</head>
<body>
<main class="flier">
  <section class="hero" role="img" aria-label="Sunset over an outback opal field dotted with pale mine mullock heaps">
    <div class="hero-fade"></div>
  </section>

  <div class="logo-badge">Trail Along Southside</div>
  <h1 class="brand">Trail Along Southside</h1>
  <ul class="contact">
    <li><svg viewBox="0 0 10 10"><circle cx="5" cy="5" r="5" fill="#f28705"/><rect x="2.3" y="3.2" width="5.4" height="3.6" fill="none" stroke="#fff" stroke-width=".7"/><path d="M2.3 3.2 5 5.3 7.7 3.2" fill="none" stroke="#fff" stroke-width=".7"/></svg>hello@trailalong.southside.example</li>
    <li><svg viewBox="0 0 10 10"><circle cx="5" cy="5" r="5" fill="#f28705"/><path d="M3.4 2.5c.4-.3.8-.2 1 .2l.4.8c.1.3 0 .5-.2.7l-.3.2c.3.7.8 1.2 1.4 1.5l.3-.3c.2-.2.4-.2.7-.1l.8.4c.4.2.5.6.2 1-.5.6-1.2.7-2 .3-1.3-.7-2.2-1.7-2.7-3-.2-.7 0-1.3.4-1.7z" fill="#fff"/></svg>08 5550 0142</li>
  </ul>

  <div class="price">$40</div>
  <div class="per"><strong>PER PERSON</strong><span>Kids half price and children under 5 FREE</span></div>

  <section class="intro">
    <p>A Unique Tag-along Journey Through Coober Pedy.</p>
    <p>Enjoy A Tour From The Comfort Of Your Own Car<br>As Our Experienced Guide Takes You Through<br>A "Day In The Life" Of A Coober Pedy Miner.</p>
  </section>

  <ul class="itinerary">
    <li class="stop"><div class="stop-photo" role="img" aria-label="Bedroom inside an underground dugout home" style="background:linear-gradient(135deg,#b89a86,#7a5a48)"></div>
      <div class="stop-text"><h3>Underground Home</h3><p>Our guide's family open the doors of their home and give you a guided tour of their dugout. See how a modern family live underground.</p></div></li>
    <li class="stop"><div class="stop-photo" role="img" aria-label="Yellow safety helmet, gloves and glasses" style="background:linear-gradient(135deg,#fff,#f4d35e)"></div>
      <div class="stop-text"><h3>Safety Gear</h3><p>All safety gear will be provided for you including helmets and UHF radios. Your safety is our number one priority!</p></div></li>
    <li class="stop"><div class="stop-photo" role="img" aria-label="Raw opal glowing blue inside rock" style="background:linear-gradient(135deg,#c99a4a,#5a5ab8)"></div>
      <div class="stop-text"><h3>Opal Mining</h3><p>We'll make our way down an underground mine where we'll show you the different techniques that modern miners use to extract this beautiful stone.</p></div></li>
    <li class="stop"><div class="stop-photo" role="img" aria-label="Danger sign in front of opal field mounds" style="background:linear-gradient(180deg,#3f6fa8,#c9c0b0 55%,#8a4e2e);height:66px"></div>
      <div class="stop-text"><h3>Drive through the field</h3><p>Making our way into town, via the opal fields, you'll get a front row seat for viewing our magical landscape that has been terraformed with over 100 years of mining. We might even pop into one of Coober Pedy's famous underground churches on our way!</p></div></li>
    <li class="stop"><div class="stop-photo" role="img" aria-label="Polished colourful opal stones" style="background:linear-gradient(135deg,#2e7a6a,#3a3a6a)"></div>
      <div class="stop-text"><h3>Noodling</h3><p>Next we hit the noodling field to try and find our own opal. With our expert guide showing you how to find opal you'll be a pro in no time!</p></div></li>
    <li class="stop"><div class="stop-photo" role="img" aria-label="Opal cutting and polishing workbench" style="background:linear-gradient(135deg,#9aa4ad,#5e6870)"></div>
      <div class="stop-text"><h3>Opal Cutting And Polishing</h3><p>We'll finish up our tour with an opal cutting and polishing demonstration and who knows?... It might be your opal we cut and polish</p></div></li>
  </ul>

  <footer class="footer">http://trailalong.southside.example</footer>
</main>
</body>
</html>
```